Business Card Design Project

Want a modern business card.
Concern is that our email address is long and thus poses a design challenge.
Items like the company name can be omitted from text as it will be available via the logo.

Example:
Gerald Tunstall
President / CEO
Cell 555.304.1182
Office 555.617.2093
geraldt@korvantsolutionsgroup.example
www.korvantsolutionsgroup.example

Target Market(s)

Technical and executive level members of Information Technology companies in the Healthcare industry.

Industry/Entity Type

Business

Colors

Designer to choose colors to be used in the design.

Requirements
Nice to have
• Raised logo, but I am open.

```html
<!DOCTYPE html>
<html lang="en">
<head>
<meta charset="utf-8">
<title>Korvant Solutions Group – Business Card</title>
<link rel="stylesheet" href="https://fonts.googleapis.com/css2?family=Cinzel:wght@700&family=Lato:wght@400;700&display=swap">
<style>
  :root {
    --backdrop: #e9e9ec;
    --card: #ffffff;
    --brand-blue: #1c3f8a;
    --brand-red: #c0161c;
    --ink: #111111;
    --divider: #9fb0cc;
  }
  * { margin: 0; padding: 0; box-sizing: border-box; }
  html, body {
    width: 1200px; height: 997px; overflow: hidden;
    background: var(--backdrop);
  }
  .canvas {
    position: relative; width: 1200px; height: 997px;
    display: flex; flex-direction: column; align-items: center; justify-content: center; gap: 50px;
  }
  .card {
    position: relative; width: 600px; height: 343px;
    background: var(--card);
    box-shadow: 0 10px 30px rgba(0,0,0,0.18);
    overflow: hidden;
  }
  .card-edge { position: absolute; left: 0; bottom: 0; width: 600px; height: 40px; }
  .company-name {
    position: absolute;
    display: flex; align-items: center;
    font-family: "Lato", sans-serif; font-weight: 700; color: var(--brand-blue);
    white-space: nowrap; line-height: 1;
  }
  .company-name::before {
    content: ""; display: block; flex: none; background: var(--brand-blue);
  }
  .card-back .company-name {
    left: 0; right: 0; top: 150px; justify-content: center; gap: 14px;
    font-size: 30px;
  }
  .card-back .company-name::before { width: 22px; height: 22px; }
  .card-front .company-name {
    left: 20px; width: 280px; top: 186px; justify-content: flex-end; gap: 8px;
    font-size: 17px;
  }
  .card-front .company-name::before { width: 12px; height: 12px; }
  .divider {
    position: absolute; left: 318px; top: 40px; width: 3px; height: 230px;
    background: linear-gradient(to bottom, var(--divider), rgba(159,176,204,0));
  }
  .contact-block { position: absolute; left: 340px; top: 52px; }
  .person-name {
    font-family: "Cinzel", serif; font-weight: 700; color: var(--brand-blue);
    font-size: 20px; letter-spacing: 0.5px;
  }
  .person-title {
    font-family: "Lato", sans-serif; font-weight: 700; color: var(--brand-red);
    font-size: 13px; margin-top: 2px;
  }
  .contact-list { list-style: none; margin-top: 38px; }
  .contact-list li {
    display: flex; align-items: center; gap: 9px; height: 24px;
    font-family: "Lato", sans-serif; font-weight: 700; font-size: 12.5px; color: var(--ink);
    white-space: nowrap;
  }
  .contact-list svg { width: 13px; height: 13px; flex: none; fill: var(--brand-blue); }
</style>
</head>
<body>
<main class="canvas">
  <section class="card card-back" aria-label="Card back">
    <div class="company-name">Korvant Solutions Group</div>
    <svg class="card-edge" viewBox="0 0 600 40" aria-hidden="true">
      <path d="M0 30 H392 Q400 30 404 40 H0 Z" fill="var(--brand-blue)"/>
      <path d="M408 40 Q412 20 432 20 H600 V40 Z" fill="var(--brand-red)"/>
    </svg>
  </section>

  <section class="card card-front" aria-label="Card front">
    <div class="company-name">Korvant Solutions Group</div>
    <div class="divider"></div>
    <div class="contact-block">
      <h1 class="person-name">GERALD TUNSTALL</h1>
      <p class="person-title">President / CEO</p>
      <ul class="contact-list">
        <li><svg viewBox="0 0 16 16"><path d="M4 1h8a1 1 0 0 1 1 1v12a1 1 0 0 1-1 1H4a1 1 0 0 1-1-1V2a1 1 0 0 1 1-1zm.5 2v9h7V3z"/></svg>555.304.1182</li>
        <li><svg viewBox="0 0 16 16"><path d="M1 6c0-2 3-3 7-3s7 1 7 3v1h-4V5.5H5V7H1zm3 2h8l2 6H2z"/></svg>555.617.2093</li>
        <li><svg viewBox="0 0 16 16"><path d="M1 3h14v10H1zm1.5 1.2L8 8.5l5.5-4.3z"/></svg>geraldt@korvantsolutionsgroup.example</li>
        <li><svg viewBox="0 0 16 16"><path d="M6 10l4-4 1 1-4 4zM3 9l2-2 1 1-2 2a1.4 1.4 0 0 0 2 2l2-2 1 1-2 2a2.8 2.8 0 0 1-4-4zm10-2l-2 2-1-1 2-2a1.4 1.4 0 0 0-2-2L8 6 7 5l2-2a2.8 2.8 0 0 1 4 4z"/></svg>www.korvantsolutionsgroup.example</li>
      </ul>
    </div>
    <svg class="card-edge" viewBox="0 0 600 40" aria-hidden="true">
      <path d="M0 30 H392 Q400 30 404 40 H0 Z" fill="var(--brand-blue)"/>
      <path d="M408 40 Q412 20 432 20 H600 V40 Z" fill="var(--brand-red)"/>
    </svg>
  </section>
</main>
</body>
</html>
```